CD Cover Design for BRISK TOFFEE

We need a groovy cover design for a new comedy CD called "Brisk Toffee." We have in mind a retro 1960s-70s feel based on the subject material of the CD, but we are open to other ideas.

In the title track, the comedian discusses candy from the past like Rosa Belles, Comet Blazers, Plum Tops, Zippy Tubes, Wax Candies, Candy Cigarettes, Candy Necklaces, etc. These specific candies do not need to be depicted, but we include them here as explanation for the name.

Target Market(s)

Men & Women, ages 25-85, but primarily over 40

Industry/Entity Type

Comedian

Requirements
Must have
• Front & Back Cover designs, both square format
• Front Cover - Title: "Brisk Toffee"
• Back Cover - Photo of Comedian (use one of the photos uploaded)
• Back Cover - Tracks listed as follows:
• 1 – Field Hockey / Parenting
• 2 – Teenagers
• 3 – Parent Teacher Conferences
• 4 – Maine
• 5 – Criminals
• 6 – Over 50
• 7 – Fun Procedure
• 8 – Guardian Donkey
• 9 – Hearthside Weekly
• 10 – 20th Anniversary
• 11 – Not a Nagger
• 12 – Travel
• 13 – Old School / Playground
• 14 – Brisk Toffee
• 15 – Cease & Desist
• 16 – Bra Shopping
• 17 – Craft Mania
• 18 – MRI Questions
• 19 – Vasectomy
Nice to have
• Retro/Vintage feel, 1960s-70s
• Original illustrations of "Brisk Toffee" would be greatly appreciated
Should not have
• Candy hearts with words

```html
<!DOCTYPE html>
<html lang="en">
<head>
<meta charset="utf-8">
<title>Brisk Toffee – CD Package</title>
<link rel="stylesheet" href="https://fonts.googleapis.com/css2?family=Sofia&family=Yellowtail&display=block">
<style>
  :root {
    --peach: #fbd6bc;
    --stripe-pink: #e9959a;
    --candy-red: #c0334e;
    --candy-red-soft: #e8787e;
    --candy-white: #fdf3f1;
    --mint: #6cc39a;
    --mint-deep: #3fa877;
    --cream: #fafad8;
    --swirl-light: #fbe0e0;
    --swirl-dark: #e8848a;
    --photo-grey: #9a9a9a;
    --ink: #2a2222;
    --page: #ffffff;
  }
  * { margin: 0; padding: 0; box-sizing: border-box; }
  html, body { width: 1200px; height: 1200px; overflow: hidden; background: var(--page); }
  .sheet { position: relative; width: 1200px; height: 1200px; }

  .script-title {
    font-family: "Yellowtail", "Brush Script MT", cursive;
    font-weight: 400;
    font-style: normal;
    line-height: 1;
    color: var(--candy-red);
    white-space: nowrap;
    -webkit-text-stroke: 2px #fff;
    paint-order: stroke fill;
    text-shadow: 0 0 1px var(--candy-red), 1px 1px 0 var(--candy-red), -1px -1px 0 var(--candy-red);
  }

  /* Front cover */
  .front-cover {
    position: absolute; left: 88px; top: 25px; width: 423px; height: 550px;
    background: repeating-linear-gradient(90deg,
      var(--peach) 0 22.4px, var(--stripe-pink) 22.4px 52px, var(--peach) 52px 58.4px);
    overflow: hidden;
  }
  .front-frame {
    position: absolute; left: 52px; top: 106px; width: 292px; height: 292px;
    border-radius: 50%;
    border: 4px solid var(--mint);
    background: var(--cream);
  }
  .lolly {
    position: absolute; border-radius: 50%;
  }
  .lolly--red {
    background: radial-gradient(circle at 50% 50%, var(--candy-white) 0 12%, #f2aeb1 40%, var(--candy-red-soft) 100%);
  }
  .lolly--green {
    background: radial-gradient(circle at 50% 50%, var(--candy-white) 0 12%, #a8dcc1 40%, var(--mint-deep) 100%);
  }
  .front-cover .lolly--red { left: 32px; top: 113px; width: 172px; height: 172px; }
  .front-cover .lolly--green { left: 170px; top: 195px; width: 140px; height: 140px; }
  .front-title {
    position: absolute; left: 22px; top: 400px; width: 380px;
    font-size: 78px; text-align: center;
    transform: rotate(-17deg);
  }

  /* Back cover */
  .back-cover {
    position: absolute; left: 690px; top: 22px; width: 424px; height: 553px;
    background: var(--peach); overflow: hidden;
  }
  .back-band { position: absolute; top: 0; width: 30px; height: 100%; background: var(--stripe-pink); }
  .back-band--left { left: 22px; }
  .back-band--right { left: 374px; }
  .track-list {
    position: absolute; left: 52px; top: 42px; list-style: none;
    font-family: "Sofia", cursive; font-size: 14.5px; line-height: 22.2px; color: var(--ink);
  }
  .back-cover .lolly--red { left: 249px; top: 256px; width: 84px; height: 84px; }
  .back-cover .lolly--green { left: 308px; top: 298px; width: 64px; height: 64px; }
  .comedian-photo {
    position: absolute; left: 198px; top: 364px; width: 164px; height: 164px;
    border-radius: 50%; border: 4px solid var(--mint);
    background: radial-gradient(circle at 50% 45%, #d4d4d4, var(--photo-grey) 70%, #5a5a5a);
  }

  /* Inside tray */
  .inside-tray {
    position: absolute; left: 92px; top: 628px; width: 418px; height: 554px;
    background: var(--peach);
  }
  .tray-cut { position: absolute; left: 0; top: 0; }

  /* Disc */
  .disc { position: absolute; left: 724px; top: 728px; width: 356px; height: 356px; }
  .disc-title {
    position: absolute; left: 744px; top: 770px; width: 320px;
    font-size: 52px; text-align: center;
    transform: rotate(9deg);
  }
</style>
</head>
<body>
<main class="sheet">

  <section class="front-cover">
    <div class="front-frame"></div>
    <div class="lolly lolly--red" role="img" aria-label="Illustration of a red and white swirl lollipop"></div>
    <div class="lolly lolly--green" role="img" aria-label="Illustration of a green and white swirl lollipop"></div>
    <h1 class="front-title script-title">Brisk Toffee</h1>
  </section>

  <section class="back-cover">
    <div class="back-band back-band--left"></div>
    <div class="back-band back-band--right"></div>
    <ol class="track-list">
      <li>1 – Field Hockey / Parenting</li>
      <li>2 – Teenagers</li>
      <li>3 – Parent Teacher Conferences</li>
      <li>4 – Maine</li>
      <li>5 – Criminals</li>
      <li>6 – Over 50</li>
      <li>7 – Fun Procedure</li>
      <li>8 – Guardian Donkey</li>
      <li>9 – Hearthside Weekly</li>
      <li>10 – 20th Anniversary</li>
      <li>11 – Not a Nagger</li>
      <li>12 – Travel</li>
      <li>13 – Old School / Playground</li>
      <li>14 – Brisk Toffee</li>
      <li>15 – Cease &amp; Desist</li>
      <li>16 – Bra Shopping</li>
      <li>17 – Craft Mania</li>
      <li>18 – MRI Questions</li>
      <li>19 – Vasectomy</li>
    </ol>
    <div class="lolly lolly--red" role="img" aria-label="Small red swirl lollipop illustration"></div>
    <div class="lolly lolly--green" role="img" aria-label="Small green swirl lollipop illustration"></div>
    <div class="comedian-photo" role="img" aria-label="Black and white childhood photo of the comedian with a sibling"></div>
  </section>

  <section class="inside-tray">
    <svg class="tray-cut" width="418" height="554" viewBox="0 0 418 554">
      <path d="M205 108 V278 A28 28 0 0 1 205 334 V504"
            fill="none" stroke="var(--candy-red)" stroke-width="5" stroke-linecap="round"/>
    </svg>
  </section>

  <svg class="disc" viewBox="0 0 356 356" role="img" aria-label="Disc face with a red and pink peppermint swirl pattern">
    <defs>
      <radialGradient id="disc-swirl" cx="50%" cy="50%" r="50%">
        <stop offset="0" stop-color="var(--swirl-light)"/>
        <stop offset="0.6" stop-color="#f1b2b5"/>
        <stop offset="1" stop-color="var(--swirl-dark)"/>
      </radialGradient>
      <mask id="disc-hole">
        <rect width="356" height="356" fill="#fff"/>
        <circle cx="178" cy="178" r="36" fill="#000"/>
      </mask>
    </defs>
    <circle cx="178" cy="178" r="178" fill="url(#disc-swirl)" mask="url(#disc-hole)"/>
  </svg>
  <p class="disc-title script-title">Brisk Toffee</p>

</main>
</body>
</html>
```